Willow Crest Website

We need a website that has clean, asian looking images that relax and motivate people to come into our integrated medical center. My current website is www.pinebrookcare.example and I would like the design for Willow Crest Health Solutions to be similar but more inviting with video content and a product purchase store as well. A moving banner would be nice too. When people are looking for ways of losing weight or getting out of pain we want them to make the connection that we have the solution. This website needs to provide sufficient information so that patients are well informed and choose us as their health provider before they ever walk through our doors. We offer comprehensive natural medicine that is based on the principles that the body can heal itself when given the right conditions. Our services include medical weight loss and hormone balancing, acupuncture and chinese herbal medicine, physical medicine, trigger point injections, allergy testing and joint rehabilitation. The Medical Doctor and Licensed Acupuncturist work as a team to provide optimal care that is catered to each individual who comes through our doors.
Updates

Target Market(s)

40 to 50 year olds who want to lose weight or have pain issues.

Industry/Entity Type

Medical

Requirements
Must have
• Use photos from our website www.pinebrookcare.example or similar content. Video content. Moving banner with relaxing images.
Nice to have
• Happy, healthy looking people. Medical Doctors working as a team. Friendly staff in a cutting edge facility.
Should not have
• Papyrus font, or big bold words.

```html
<!DOCTYPE html>
<html lang="en">
<head>
<meta charset="utf-8">
<title>Willow Crest Health Solutions – About us</title>
<link href="https://fonts.googleapis.com/css2?family=Maven+Pro:wght@400;500;700&display=swap" rel="stylesheet">
<style>
:root{
  --wood:#ece4d5;
  --wood-line:#e2d8c6;
  --band-top:#ddd0b6;
  --band-bottom:#e9dfcc;
  --olive:#9c9876;
  --olive-dark:#7d7a5c;
  --text:#7a6a5c;
  --heading:#6e6052;
  --nav:#a89a88;
  --footer:#867669;
  --footer-text:#efe6d8;
  --contact:#c4bc9f;
  --contact-text:#5e5448;
  --menu-line:#9d9282;
  --menu-active:#dccfbd;
  --thumb-border:#8a7466;
}
*{box-sizing:border-box;margin:0;padding:0}
html,body{width:1000px;height:1200px;overflow:hidden}
body{
  position:relative;
  font-family:"Maven Pro",sans-serif;
  color:var(--text);
  background:var(--wood) repeating-linear-gradient(180deg,transparent 0 35px,var(--wood-line) 35px 36px);
}
.abs{position:absolute}
.top-band{left:0;top:76px;width:1000px;height:73px;background:linear-gradient(180deg,var(--band-top),var(--band-bottom));box-shadow:inset 0 3px 4px rgba(0,0,0,.12)}
.main-nav{right:131px;top:46px;display:flex;gap:21px;font-size:9px;font-weight:700;letter-spacing:1px;text-transform:uppercase}
.main-nav a{color:var(--nav);text-decoration:none}
.main-nav a.current{color:var(--heading);border-bottom:1px solid var(--heading);padding-bottom:2px;position:relative}
.main-nav a.current::after{content:"";position:absolute;left:50%;top:19px;margin-left:-6px;border:6px solid transparent;border-top-color:var(--wood)}
.brand{left:131px;top:56px;width:175px;height:234px;background:var(--olive);box-shadow:2px 2px 4px rgba(0,0,0,.15);text-align:center;color:#fff}
.brand::before{content:"";position:absolute;left:-9px;top:0;border-bottom:14px solid var(--olive-dark);border-left:9px solid transparent}
.brand-art{position:absolute;left:19px;top:20px;width:137px;height:146px;background:linear-gradient(180deg,#d6cfbc,#a8a385)}
.brand-name{position:absolute;left:0;right:0;top:174px;font-size:27px;font-weight:700;line-height:1}
.brand-sub{position:absolute;left:0;right:0;top:208px;font-size:11.5px;font-weight:400;letter-spacing:.5px}
.page-title{left:333px;top:92px;font-size:31px;font-weight:400;color:var(--heading)}
.lead,.body-copy{font-size:10.5px;line-height:19px;width:538px;left:331px}
.lead{top:172px}
.side-menu{left:131px;top:318px;width:175px;list-style:none;font-size:13px}
.side-menu li{height:37.5px;line-height:37px;padding-left:7px;border-top:1px solid var(--menu-line)}
.side-menu li:last-child{border-bottom:1px solid var(--menu-line)}
.side-menu li.current{background:var(--menu-active);font-weight:700}
.video{left:331px;top:262px;width:538px;height:263px;border:1px solid var(--thumb-border);background:linear-gradient(180deg,#8a8078 0%,#a29890 45%,#d49a72 65%,#c88762 100%)}
.play{position:absolute;left:50%;top:50%;transform:translate(-50%,-50%)}
.team-band{left:0;top:562px;width:1000px;height:125px;background:linear-gradient(180deg,#e5d9c3,#ece4d5)}
.team-text{left:131px;top:580px;width:170px;font-size:18.5px;line-height:38px;color:var(--heading)}
.thumb{top:590px;width:113px;height:76px;border:1px solid var(--thumb-border)}
.thumb .play{transform:translate(-50%,-50%) scale(.55)}
.t1{left:331px;background:linear-gradient(135deg,#3c3633,#b68a6c)}
.t2{left:472px;background:linear-gradient(135deg,#7a5a42,#3b2e28)}
.t3{left:614px;background:linear-gradient(180deg,#151313 40%,#c07c58)}
.t4{left:756px;background:linear-gradient(135deg,#0d0c0c 30%,#b9806a)}
.copy1{top:739px}
.copy2{top:813px}
.site-footer{left:0;top:937px;width:1000px;height:224px;background:var(--footer);border-top:1px solid #a39486;box-shadow:inset 0 2px 3px rgba(0,0,0,.15)}
.foot-col{top:965px;width:111px;list-style:none;font-size:8.5px;line-height:19px;color:var(--footer-text)}
.foot-col li::before{content:"• "}
.foot-col .head{font-weight:700;text-transform:uppercase;letter-spacing:.5px}
.foot-col .gap{border-top:1px dotted #cbbfae;margin:6px 0 8px;height:0;line-height:0}
.foot-col .gap::before{content:""}
.col1{left:131px}.col2{left:257px}.col3{left:381px}
.ornament{left:541px;top:955px;width:44px;height:178px;background:linear-gradient(180deg,rgba(110,95,84,.55),rgba(110,95,84,.35))}
.contact-card{left:631px;top:919px;width:238px;height:150px;background:var(--contact);box-shadow:2px 3px 5px rgba(0,0,0,.25);padding:10px 13px;color:var(--contact-text)}
.contact-card::before{content:"";position:absolute;left:-11px;top:0;border-bottom:18px solid #ab9f85;border-left:11px solid transparent}
.contact-card h2{font-size:17px;font-weight:700;margin-bottom:3px}
.contact-card p{font-size:10.5px;line-height:19px;color:#f4eee2}
.contact-line{display:flex;align-items:center;gap:6px;font-size:12px;font-weight:700;margin-top:8px}
.social{top:1091px;left:714px;display:flex;gap:14px}
.social span{width:28px;height:28px;border-radius:50%;background:#5b4d44;box-shadow:0 1px 2px rgba(0,0,0,.3)}
.copyright{left:131px;top:1173px;font-size:10px;color:var(--heading)}
</style>
</head>
<body>

<nav class="abs main-nav">
  <a href="#">Home</a><a href="#" class="current">About us</a><a href="#">Acupuncture</a><a href="#">Healthcare</a><a href="#">Shop</a><a href="#">Contact</a>
</nav>

<div class="abs top-band"></div>

<div class="abs brand">
  <div class="brand-art" role="img" aria-label="Illustration of a windswept tree on a rocky hill"></div>
  <div class="brand-name">Willow Crest</div>
  <div class="brand-sub">HEALTH SOLUTIONS</div>
</div>

<h1 class="abs page-title">About us</h1>
<p class="abs lead">sse per sesars tam exptendu quam nostros expetere quo loco visetur quibusing stabilit amicitaie acillard tuent tamet eum locum seque facil, ut mihi detur expedium. It enim vitutes Lorem ipsum dolor sit amet, consectetur adipscing elit, sed diam nonnumy eiusmod tempor incidunt ut labore et dolore.</p>

<ul class="abs side-menu">
  <li>Philosophy</li>
  <li>History</li>
  <li class="current">Videao</li>
</ul>

<div class="abs video" role="img" aria-label="Video still of acupuncture needles placed along a patient's back">
  <svg class="play" width="52" height="52" viewBox="0 0 52 52"><circle cx="26" cy="26" r="24" fill="#cfc6bd" stroke="#8a7e74" stroke-width="2"/><path d="M20 15 L37 26 L20 37 Z" fill="#6d625a"/></svg>
</div>

<div class="abs team-band"></div>
<p class="abs team-text">Our team is autem vel eum irure dolor in.</p>

<div class="abs thumb t1" role="img" aria-label="Video still of hands placing acupuncture needles"><svg class="play" width="52" height="52" viewBox="0 0 52 52"><circle cx="26" cy="26" r="24" fill="#cfc6bd" stroke="#333" stroke-width="3"/><path d="M20 15 L37 26 L20 37 Z" fill="#555"/></svg></div>
<div class="abs thumb t2" role="img" aria-label="Video still of acupuncture treatment on the head"><svg class="play" width="52" height="52" viewBox="0 0 52 52"><circle cx="26" cy="26" r="24" fill="#cfc6bd" stroke="#333" stroke-width="3"/><path d="M20 15 L37 26 L20 37 Z" fill="#555"/></svg></div>
<div class="abs thumb t3" role="img" aria-label="Video still of a needle on a patient's back"><svg class="play" width="52" height="52" viewBox="0 0 52 52"><circle cx="26" cy="26" r="24" fill="#cfc6bd" stroke="#333" stroke-width="3"/><path d="M20 15 L37 26 L20 37 Z" fill="#555"/></svg></div>
<div class="abs thumb t4" role="img" aria-label="Video still of a needle placed in a hand"><svg class="play" width="52" height="52" viewBox="0 0 52 52"><circle cx="26" cy="26" r="24" fill="#cfc6bd" stroke="#333" stroke-width="3"/><path d="M20 15 L37 26 L20 37 Z" fill="#555"/></svg></div>

<p class="abs body-copy copy1">Hecessit atib saepe eveniet ut er repudiand sint et molestia non recus. Itaque earud reruam hist entaury sapiente delecatus auaut prefear enrdis dolorib asperiore repellat. Hanc ego cum tene sententiam, quid est cur verear ne ad eam non possing accommodare nost ros quos.</p>
<p class="abs body-copy copy2">tu paulo ante cum memorie tum etia ergat. Nos amice et nebevol, olestias access potest fier ad augendas cum conscient to factor tum poen legum odioque cividua. Et tamen in busa.</p>

<footer class="abs site-footer"></footer>

<ul class="abs foot-col col1">
  <li class="head">Home</li>
  <li class="gap"></li>
  <li class="head">About us</li>
  <li>Philosophy</li>
  <li>Our team</li>
</ul>
<ul class="abs foot-col col2">
  <li class="head">Acupuncture</li>
  <li>Information</li>
  <li>History</li>
  <li>Seitai Shinpo</li>
  <li class="gap"></li>
  <li class="head">Healthcare</li>
  <li>Programme</li>
  <li>So Tai Ho</li>
  <li>Therapy</li>
</ul>
<ul class="abs foot-col col3">
  <li class="head">Shop</li>
  <li>Massage Oil</li>
  <li>Therapeutics</li>
  <li>Herbal</li>
  <li>Beauty products</li>
  <li class="gap"></li>
  <li class="head">Contact</li>
</ul>

<div class="abs ornament" role="img" aria-label="Faint vertical brush calligraphy wishing health and happiness"></div>

<section class="abs contact-card">
  <h2>Contact us</h2>
  <p>Lorem ipsum do pland sit amet, con sectetur a dip sching.</p>
  <div class="contact-line">
    <svg width="12" height="22" viewBox="0 0 12 22"><rect x="1" y="1" width="10" height="20" rx="2" fill="none" stroke="#5e5448" stroke-width="1.8"/><rect x="3" y="4" width="6" height="7" fill="#5e5448"/><circle cx="6" cy="16" r="1.6" fill="#5e5448"/></svg>
    (555) 014-2290
  </div>
  <div class="contact-line">
    <svg width="15" height="12" viewBox="0 0 15 12"><rect x="0.5" y="0.5" width="14" height="11" fill="#5e5448"/><path d="M1 1 L7.5 7 L14 1" fill="none" stroke="#c4bc9f" stroke-width="1.4"/></svg>
    info@willowcrest.example
  </div>
</section>

<div class="abs social" aria-label="Social links"><span></span><span></span><span></span><span></span></div>

<p class="abs copyright">© Copyright Willow Crest Healthcare 2012 - Privacy policy</p>

</body>
</html>
```